"We Are Hiring" Flyer

I am needing a flyer made for hiring. below is what we would like to have on it as well as our a logo and ive attached a QR code that will link to our jobwick job listing if that can be included as well.
We Are Hiring!
Branch Manager
Starting pay $21-$23 per hour + monthly bonuses + Health Insurance
Reach out to us: info@tallowcrest.com
(about us) Tallowcrest Financial is a different kind of loan company. We understand just how important a loan is to the lives and futures of our clients. Tallowcrest Financial offers flexible payment options and competitive loan rates to ensure that our clients have the best possible experience.
8.5” x 11”
Industry/Entity Type
Finance
Look and feel
Each slider illustrates characteristics of the customer's brand and the style your logo design should communicate.

```html
<!DOCTYPE html>
<html lang="en">
<head>
<meta charset="utf-8">
<title>We Are Hiring – Tallowcrest Financial</title>
<link rel="stylesheet" href="https://fonts.googleapis.com/css2?family=Montserrat:wght@400;500;600;700&display=swap">
<style>
  :root {
    --page-bg: #e0e0e0;
    --frame-grey: #6f6a6a;
    --forest: #265a3b;
    --forest-soft: #487a5a;
    --sage: #84a585;
    --ink-green: #1f4a2e;
    --cream: #fbf9e6;
    --crimson: #b32e30;
    --crimson-soft: #cf4a4a;
    --crimson-deep: #c11f26;
  }
  * { margin: 0; padding: 0; box-sizing: border-box; }
  html, body {
    width: 900px; height: 1200px; overflow: hidden;
    background: var(--page-bg);
    font-family: "Montserrat", Arial, sans-serif;
  }
  .flyer {
    position: absolute; left: 88px; top: 111px;
    width: 720px; height: 930px; overflow: hidden;
    background: var(--frame-grey);
  }
  .flyer-shapes { position: absolute; inset: 0; }
  .headline {
    position: absolute; left: 100px; top: 150px; width: 340px;
    text-align: center; color: var(--cream); line-height: 1;
  }
  .headline-small { display: block; font-size: 41px; font-weight: 600; letter-spacing: 1px; }
  .headline-big { display: block; font-size: 73px; font-weight: 700; margin-top: 10px; }
  .brand {
    position: absolute; left: 470px; top: 262px; width: 180px;
    display: flex; align-items: center; gap: 8px;
    color: var(--forest); font-size: 15px; font-weight: 600; letter-spacing: 0.5px;
  }
  .brand-square { width: 14px; height: 14px; background: var(--crimson-deep); flex: none; }
  .info-table {
    position: absolute; left: 93px; top: 428px; width: 528px;
    display: flex; flex-direction: column; gap: 9px;
  }
  .info-label, .info-value {
    display: flex; flex-direction: column; justify-content: center; align-items: center;
    text-align: center; text-transform: uppercase; letter-spacing: 1.8px;
  }
  .info-label {
    height: 44px; border: 1.5px solid var(--ink-green);
    color: var(--ink-green); font-size: 17px; font-weight: 600;
  }
  .info-value {
    min-height: 44px; background: var(--sage);
    color: var(--cream); font-size: 20px; font-weight: 500; line-height: 1.2;
  }
  .info-value.pay { height: 71px; font-size: 19px; }
  .contact {
    position: absolute; left: 0; width: 716px; top: 725px;
    text-align: center; color: var(--cream);
  }
  .contact-lead { font-size: 12px; }
  .contact-email { font-size: 18px; font-weight: 500; margin-top: 6px; }
  .about {
    position: absolute; left: 110px; top: 822px; display: flex; gap: 14px;
    color: var(--cream);
  }
  .about-title {
    width: 76px; text-align: right; font-size: 14px; font-weight: 700;
    line-height: 1.3; padding-top: 20px; padding-right: 14px;
    border-right: 2px solid var(--cream); height: 76px;
  }
  .about-text { width: 385px; font-size: 11.2px; line-height: 1.3; padding-top: 2px; }
</style>
</head>
<body>
  <main class="flyer">
    <svg class="flyer-shapes" width="720" height="930" viewBox="0 0 720 930" aria-hidden="true">
      <defs>
        <clipPath id="panel-clip"><rect x="81" y="112" width="554" height="679"/></clipPath>
        <clipPath id="below-panel"><rect x="0" y="791" width="720" height="139"/></clipPath>
      </defs>
      <path class="red-swoosh" d="M0 300 Q180 380 460 255 Q300 440 0 395 Z" fill="var(--crimson-deep)"/>
      <ellipse class="green-disc" cx="240" cy="40" rx="312" ry="310" fill="var(--forest)"/>
      <rect class="cream-panel" x="81" y="112" width="554" height="679" fill="var(--cream)"/>
      <g clip-path="url(#panel-clip)">
        <path d="M0 300 Q180 380 460 255 Q300 440 0 395 Z" fill="var(--crimson-deep)"/>
        <ellipse cx="240" cy="40" rx="312" ry="310" fill="var(--forest-soft)"/>
        <circle class="red-disc-soft" cx="358" cy="980" r="294" fill="var(--crimson-soft)"/>
      </g>
      <circle class="red-disc" cx="358" cy="980" r="294" fill="var(--crimson)" clip-path="url(#below-panel)"/>
    </svg>

    <h1 class="headline">
      <span class="headline-small">WE ARE</span>
      <span class="headline-big">HIRING!</span>
    </h1>

    <div class="brand"><span class="brand-square"></span>Tallowcrest Financial</div>

    <section class="info-table">
      <div class="info-label">Position</div>
      <div class="info-value">Branch Manager</div>
      <div class="info-label">Starting Pay</div>
      <div class="info-value pay">
        <span>$21 - $23 per hour</span>
        <span>Monthly bonuses + health insurance</span>
      </div>
    </section>

    <section class="contact">
      <p class="contact-lead">Reach out to us:</p>
      <p class="contact-email">info@tallowcrest.com</p>
    </section>

    <section class="about">
      <h2 class="about-title">ABOUT US</h2>
      <p class="about-text">Tallowcrest Financial is a different kind of loan company. We understand just how important a loan is to the lives and futures of our clients. Tallowcrest Financial offers flexible payment options and competitive loan rates to ensure that our clients have the best possible experience.</p>
    </section>
  </main>
</body>
</html>
```